Quotation and Scripture Design

We are a marketing firm looking for a graphic designer who is gifted in the merging of typestyles, colors, and composition into images suitable for framing in the home or office. The design criteria is quite simple, (1) keep it fresh without looking dated or religious, and (2) push the envelope a little with good, solid graphic design. Phase one will involve building our inventory of original artwork to fifty or more pieces to be marketed online. For phase two in addition to a line of greeting cards, we will also offer art pieces reproduced by laser engravers, CNC routers, chemical etching, and digital printers. For this reason it is necessary that all art files be submitted in a vector format.

Target Market(s)

Professional women and men who appreciate and purchase gallery quality artwork.

Industry/Entity Type

Graphic Designer

Requirements
Must have
• Selection of the designer will be based on their graphic interruption of the following two quotations.
Quotation No. 1 - Romans 8:28
And we know that all things work together for good to those who love God, to those who are called according to His purpose.
Quotation No. 2 -Jeremiah 29:11
For I know the plans I have for you, declares the Lord. Plans to prosper you and not to harm you. Plans to give you hope and a future.
Design one of these two formats to fit a 8" x10" frame, and the other to fit a 12" x 12" frame.
Nice to have
• Rich colors, fresh typestyles . . . please no Times Roman. Bold, creative composition is what we are looking for.
Should not have
• Dated, religious artwork found in the local bible bookstore is a very good example of what we DO NOT want. If it is not something you would purchase for yourself or a friend, more than likely it won't meet our criteria.

```html
<!DOCTYPE html>
<html lang="en">
<head>
<meta charset="UTF-8">
<title>Romans 8:28 — Framed Verse</title>
<link href="https://fonts.googleapis.com/css2?family=Handlee&display=swap" rel="stylesheet">
<style>
  :root {
    --earth-brown: #6f4527;
    --leaf-green: #8dc63f;
    --stem-yellow: #f2e600;
    --petal-white: #ffffff;
  }
  html, body {
    margin: 0;
    padding: 0;
    overflow: hidden;
    background: var(--earth-brown);
  }
  .artwork {
    position: relative;
    width: 960px;
    height: 1200px;
    overflow: hidden;
    background: var(--earth-brown);
    font-family: "Handlee", cursive;
    color: var(--leaf-green);
  }
  .verse {
    margin: 0;
  }
  .verse-line {
    position: absolute;
    display: block;
    white-space: nowrap;
    font-size: 86px;
    line-height: 1;
    transform: skewX(-6deg);
  }
  .line-1 { left: 30px;  top: 96px; }
  .line-2 { left: 22px;  top: 256px; }
  .line-3 { left: 12px;  top: 426px; }
  .line-4 { left: 14px;  top: 606px; }
  .line-5 { left: 12px;  top: 786px; }
  .line-6 { left: 10px;  top: 966px; }
  .reference {
    position: absolute;
    left: 566px;
    top: 1098px;
    font-size: 44px;
    line-height: 1;
    transform: skewX(-6deg);
  }
  .botanical {
    position: absolute;
    right: 0;
    top: 0;
    width: 260px;
    height: 1200px;
    background: linear-gradient(180deg,
      rgba(141, 198, 63, 0) 0%,
      rgba(141, 198, 63, 0.35) 25%,
      rgba(141, 198, 63, 0.6) 60%,
      rgba(242, 230, 0, 0.45) 100%);
  }
</style>
</head>
<body>
  <main class="artwork">
    <div class="botanical" role="img" aria-label="Slender green leafy stems with white and yellow grass blades rising along the right edge"></div>
    <blockquote class="verse">
      <span class="verse-line line-1">And we know</span>
      <span class="verse-line line-2">that all&nbsp; things</span>
      <span class="verse-line line-3">work together for good,</span>
      <span class="verse-line line-4">to those who love God,</span>
      <span class="verse-line line-5">to those who are called</span>
      <span class="verse-line line-6">according to His purpose.</span>
    </blockquote>
    <cite class="reference">Romans 8:28</cite>
  </main>
</body>
</html>
```